Web Page for marketing online agency

We are an online marketing agency that is acing the direct response model. We engage with our customers throughout different marketing techniques as research copy-writing, advertisements and content writing. We would need a website design that will have four main aspects: The Vision; stating who we are, The Mission; stating what we do, The Team And It's Values, and a Contact Form. For this design we would want a sharp, clean and smart approach, with illustrated elements or suggestive images. You can use the attached copy, the logo, the USP and the motto. Please integrate them as you see fit while keeping in mind the previous needs and copy. This website is going to be our connection with our possible partners, future colleagues and even our clients. You may submit a design for one page or integrate the 4 different aspects on separate web pages.
Target Market(s)
business partners, future employees, age range 25-60
Industry/Entity Type
Direct Marketing
Number of Pages Required
1 page
Requirements
Must have
- Menu / Header
- 4 Parts or 4 Pages including: vision, mission, team, contact
- Logo
- Motto: Direct Brilliance
- USP: We help people help themselves.
- The copy attached
Nice to have
- Representative illustrated images or elements
Should not have
- A boring design, classical design - Pagequill like

```html
<!DOCTYPE html>
<html lang="en">
<head>
<meta charset="utf-8">
<title>Brightlane – Direct Brilliance</title>
<link href="https://fonts.googleapis.com/css2?family=Raleway:ital,wght@0,300;0,400;0,500;0,600;0,700;1,300;1,400&display=swap" rel="stylesheet">
<style>
:root{
  --sky:#4db4ef;
  --sky-deep:#2f9ee2;
  --sky-light:#a9dcf8;
  --ink:#1f2228;
  --text:#4a4f57;
  --muted:#8d939b;
  --paper:#ffffff;
  --mist:#f3f4f6;
  --field:#eef0f3;
  --night:#232427;
  --night-deep:#1a1b1d;
  --night-line:#3a3b3f;
  --accent:#f4c531;
}
*{margin:0;padding:0;box-sizing:border-box}
html,body{width:1200px;height:3692px;overflow:hidden}
body{font-family:'Raleway',sans-serif;color:var(--text);background:var(--paper);position:relative}
section,header,footer{position:relative;width:1200px}
.eyebrow{font-style:italic;font-weight:300;color:var(--muted);font-size:17px;text-align:center}
.section-title{font-size:42px;font-weight:700;color:var(--ink);text-align:center;margin-top:10px}
.section-title em{font-weight:300;font-style:italic}

/* hero */
.hero{height:700px;background:linear-gradient(180deg,var(--sky) 0%,#5cbcf1 100%);overflow:hidden}
.topbar{height:30px;background:var(--sky-deep);display:flex;align-items:center;padding:0 20px;color:#fff;font-size:12px;gap:26px}
.topbar .social{margin-left:auto;display:flex;gap:12px}
.topbar .social span{width:10px;height:10px;border-radius:50%;background:#fff;opacity:.85}
.navbar{height:90px;display:flex;align-items:center;padding:0 60px}
.brand{display:flex;align-items:center;gap:10px;color:#fff;font-size:30px;font-weight:700}
.brand .dot{width:22px;height:22px;border-radius:50%;background:var(--accent)}
.menu{display:flex;gap:0;margin-left:90px;list-style:none}
.menu li{font-size:12px;font-weight:600;color:#fff;letter-spacing:1px;padding:12px 24px}
.menu li.active{background:rgba(255,255,255,.22)}
.nav-tools{margin-left:auto;display:flex;gap:20px}
.nav-tools svg{width:18px;height:18px}
.hero-copy{position:absolute;left:166px;top:250px;width:520px;color:#fff}
.hero-copy h1{font-size:58px;font-weight:500;line-height:1.1}
.hero-copy p{margin-top:28px;font-size:16px;line-height:1.7}
.hero-actions{margin-top:42px;display:flex;gap:18px}
.btn{display:inline-block;font-size:12px;font-weight:700;letter-spacing:1px;padding:15px 36px;color:#fff}
.btn.dark{background:var(--ink)}
.btn.line{border:2px solid #fff}
.hero-art{position:absolute;left:700px;top:110px;width:420px;height:520px;border-radius:30px;background:radial-gradient(circle at 50% 45%,#d8f0fd 0%,#8fd1f6 55%,rgba(143,209,246,0) 75%)}
.slider-arrow{position:absolute;top:330px;width:40px;height:40px;background:#fff;display:flex;align-items:center;justify-content:center}
.slider-arrow.left{left:0}.slider-arrow.right{right:0}
.slider-dots{position:absolute;top:660px;left:0;width:100%;display:flex;justify-content:center;gap:8px}
.slider-dots span{width:8px;height:8px;border-radius:50%;background:rgba(255,255,255,.55)}
.slider-dots span:first-child{background:#fff}

/* values */
.values{height:536px;padding-top:90px}
.value-row{display:flex;justify-content:center;gap:48px;margin-top:70px}
.value{width:230px;text-align:center}
.value-icon{width:120px;height:120px;margin:0 auto;border-radius:50%}
.value h3{font-size:17px;font-weight:600;color:var(--ink);margin-top:28px}
.value p{font-size:12px;color:var(--muted);line-height:1.6;margin-top:10px}

/* who */
.who{height:572px;background:var(--mist);padding-top:42px}
.who .section-title{font-size:40px}
.card-row{display:flex;justify-content:center;gap:22px;margin-top:46px}
.card{width:317px;height:370px;position:relative}
.card-image{height:215px}
.card-body{position:absolute;left:24px;right:24px;top:196px;background:#fff;padding:26px 20px;text-align:center}
.card-body h3{font-size:18px;font-weight:600;color:var(--ink)}
.card-body p{font-size:13px;line-height:1.55;margin-top:14px}

/* team */
.team{height:469px;padding-top:60px}
.team .section-title{font-size:40px}
.members{display:flex;margin-top:76px;padding-left:137px;gap:124px}
.member{display:flex;gap:22px;width:380px}
.member-photo{width:166px;height:166px;flex:none}
.member h3{font-size:17px;font-weight:700;color:var(--ink);margin-top:6px}
.member .role{font-size:12px;color:var(--muted);margin-top:4px}
.member p{font-size:12px;line-height:1.6;margin-top:12px}
.member .links{display:flex;gap:14px;margin-top:20px}
.member .links span{width:11px;height:11px;border-radius:50%;background:var(--muted)}

/* testimonial */
.testimonial{height:336px;background:var(--sky);overflow:hidden}
.testimonial-photo{position:absolute;left:0;top:0;width:650px;height:336px}
.testimonial blockquote{position:absolute;left:683px;top:62px;width:440px;color:#fff;font-size:27px;font-weight:600;line-height:1.45}

/* contact */
.contact{height:542px;padding-top:40px}
.contact .section-title{font-size:42px;margin-top:14px}
.contact-form{position:absolute;left:63px;top:192px;width:1099px;height:240px;background:var(--field);display:flex}
.form-col{width:50%;border-right:1px solid #dde0e5}
.form-col:last-child{border-right:none}
.field{height:80px;border-bottom:1px solid #dde0e5;padding:26px 28px;font-size:13px;color:var(--muted)}
.form-col:last-child .field{height:240px;border-bottom:none}
.submit{position:absolute;left:527px;top:457px;width:146px;height:38px;background:var(--sky);color:#fff;font-size:12px;font-weight:700;letter-spacing:1px;display:flex;align-items:center;justify-content:center}

/* footer */
.follow{height:185px;background:var(--night);text-align:center;padding-top:52px;color:#fff}
.follow h4{font-size:14px;font-weight:600}
.follow .circles{display:flex;justify-content:center;gap:16px;margin-top:24px}
.follow .circles span{width:44px;height:44px;border:2px solid #777;border-radius:50%}
.site-footer{height:315px;background:var(--night-deep);color:#9a9ea4}
.footer-grid{display:flex;padding:80px 0 0 103px}
.footer-brand{width:266px}
.footer-brand .brand{font-size:28px}
.footer-brand p{font-size:11px;line-height:1.6;margin-top:16px;width:200px}
.footer-col{width:250px}
.footer-col h5{font-size:12px;font-weight:700;color:#fff;letter-spacing:1px;margin-bottom:18px}
.footer-col ul{list-style:none;font-size:11px;line-height:2.1;columns:2;width:170px}
.footer-col.info ul{columns:1}
.footer-col p{font-size:11px;line-height:1.6;width:200px}
.newsletter{margin-top:36px;width:210px;border-bottom:1px solid var(--night-line);font-size:11px;padding-bottom:8px}
.copyright{position:absolute;left:0;bottom:0;width:100%;height:37px;background:#111214;font-size:11px;display:flex;align-items:center;justify-content:center;color:#7d8187}
.copyright b{color:#fff;margin:0 4px}
</style>
</head>
<body>

<section class="hero">
  <div class="topbar"><span>+1 415 555 0142</span><span>hello@brightlane.co</span><div class="social"><span></span><span></span><span></span></div></div>
  <header class="navbar">
    <div class="brand"><span>Brightlane</span><span class="dot"></span></div>
    <ul class="menu"><li class="active">HOME</li><li>ABOUT</li><li>SERVICES</li><li>BLOG</li><li>CONTACT</li></ul>
    <div class="nav-tools">
      <svg viewBox="0 0 18 18"><circle cx="8" cy="8" r="5.5" fill="none" stroke="#fff" stroke-width="2"/><line x1="12" y1="12" x2="16" y2="16" stroke="#fff" stroke-width="2"/></svg>
      <svg viewBox="0 0 18 18"><g stroke="#fff" stroke-width="2"><line x1="2" y1="4" x2="16" y2="4"/><line x1="2" y1="9" x2="16" y2="9"/><line x1="2" y1="14" x2="16" y2="14"/></g></svg>
    </div>
  </header>
  <div class="hero-copy">
    <h1>We help people<br>help themselves.</h1>
    <p>We are a direct response company that creates and sells information products and services that millions of people find interesting and important in their lives.</p>
    <div class="hero-actions"><span class="btn dark">CONTACT US</span><span class="btn line">INFORMATION</span></div>
  </div>
  <div class="hero-art" role="img" aria-label="Illustration of an open parcel box releasing a lightbulb, paper plane and floating ideas"></div>
  <div class="slider-arrow left"><svg width="12" height="12" viewBox="0 0 12 12"><path d="M8 1 3 6l5 5" fill="none" stroke="#333" stroke-width="2"/></svg></div>
  <div class="slider-arrow right"><svg width="12" height="12" viewBox="0 0 12 12"><path d="M4 1l5 5-5 5" fill="none" stroke="#333" stroke-width="2"/></svg></div>
  <div class="slider-dots"><span></span><span></span><span></span></div>
</section>

<section class="values">
  <p class="eyebrow">A World of Opportunities</p>
  <h2 class="section-title">Our <em>Core Values</em></h2>
  <div class="value-row">
    <div class="value"><div class="value-icon" role="img" aria-label="Illustration of a stopwatch with gears" style="background:radial-gradient(circle,#9fd6f7,#e8f5fd)"></div><h3>Fairness</h3><p>Every partner gets honest terms and clear answers from the very first call.</p></div>
    <div class="value"><div class="value-icon" role="img" aria-label="Illustration of a hand holding a magnifying glass" style="background:radial-gradient(circle,#f5d77a,#fdf6e0)"></div><h3>Caring</h3><p>We listen closely to customers and shape every offer around real needs.</p></div>
    <div class="value"><div class="value-icon" role="img" aria-label="Illustration of a stopwatch" style="background:radial-gradient(circle,#c8cdd3,#f3f4f6)"></div><h3>Safety</h3><p>Data and budgets are handled with care and full transparency at all times.</p></div>
    <div class="value"><div class="value-icon" role="img" aria-label="Illustration of a padlock in front of a globe" style="background:radial-gradient(circle,#7fc7ef,#e2f3fc)"></div><h3>Freedom</h3><p>Our people choose how they work and grow with room for fresh ideas.</p></div>
  </div>
</section>

<section class="who">
  <p class="eyebrow">Firm in the Field of Marketing</p>
  <h2 class="section-title">Who <em>We Are</em></h2>
  <div class="card-row">
    <div class="card"><div class="card-image" role="img" aria-label="Photo of a hand holding a glowing lightbulb" style="background:linear-gradient(135deg,#2b2b2e,#6b5a3d)"></div><div class="card-body"><h3>Our Vision</h3><p>We are a direct response company that creates and sells information products and services that millions of people find interesting and important in their lives.</p></div></div>
    <div class="card"><div class="card-image" role="img" aria-label="Photo of a mission sign with a target" style="background:linear-gradient(135deg,#d9d9d9,#8b8f94)"></div><div class="card-body"><h3>Our Mission</h3><p>We are a direct response company that creates and sells information products and services that millions of people find interesting and important in their lives.</p></div></div>
    <div class="card"><div class="card-image" role="img" aria-label="Photo of darts hitting a dartboard" style="background:linear-gradient(135deg,#e8a45c,#5a3a2a)"></div><div class="card-body"><h3>Our Goals</h3><p>We are a direct response company that creates and sells information products and services that millions of people find interesting and important in their lives.</p></div></div>
  </div>
</section>

<section class="team">
  <p class="eyebrow">Growing your Business</p>
  <h2 class="section-title">The Team &amp; Value <em>That You Need</em></h2>
  <div class="members">
    <div class="member"><div class="member-photo" role="img" aria-label="Portrait photo of Mara Colt" style="background:linear-gradient(160deg,#d7d4cf,#9a948c)"></div><div><h3>Mara Colt</h3><div class="role">CEO &amp; Founder</div><p>Mara started her career in direct response and built a team that lives for copywriting.</p><div class="links"><span></span><span></span><span></span><span></span></div></div></div>
    <div class="member"><div class="member-photo" role="img" aria-label="Portrait photo of Devin Holt" style="background:linear-gradient(160deg,#c9b9a2,#4a3d32)"></div><div><h3>Devin Holt</h3><div class="role">Growth &amp; Affiliate Manager</div><p>Devin runs our partner network and grows it with trusted affiliates every month.</p><div class="links"><span></span><span></span><span></span><span></span></div></div></div>
  </div>
</section>

<section class="testimonial">
  <svg class="testimonial-photo" viewBox="0 0 650 336" role="img" aria-label="Photo of a smiling client with curly hair">
    <defs><linearGradient id="clientTone" x1="0" y1="0" x2="1" y2="1"><stop offset="0" stop-color="#e9d6bf"/><stop offset="1" stop-color="#b98a5e"/></linearGradient></defs>
    <polygon points="0,0 650,0 470,336 0,336" fill="url(#clientTone)"/>
  </svg>
  <blockquote>I have only the best to say about this company. They are always on time, and always fulfill the expectations entirely.</blockquote>
</section>

<section class="contact">
  <p class="eyebrow">Higher Faster Stronger</p>
  <h2 class="section-title">Contact Our <em>Awesome Team</em></h2>
  <div class="contact-form">
    <div class="form-col"><div class="field">First Name</div><div class="field">Last Name</div><div class="field">Your E-mail address</div></div>
    <div class="form-col"><div class="field">Write your message</div></div>
  </div>
  <div class="submit">CONTACT US</div>
</section>

<section class="follow">
  <h4>Follow Us</h4>
  <div class="circles"><span></span><span></span><span></span><span></span></div>
</section>

<footer class="site-footer">
  <div class="footer-grid">
    <div class="footer-brand"><div class="brand"><span>Brightlane</span><span class="dot"></span></div><p>Direct Brilliance. A small team that turns research and copy into results.</p></div>
    <div class="footer-col"><h5>SITEMAP</h5><ul><li>Home</li><li>About</li><li>Services</li><li>Blog</li><li>Contact</li></ul></div>
    <div class="footer-col info"><h5>CONTACT INFO</h5><ul><li>220 Harbor Street, Suite 14</li><li>Fairview, OR 97024</li><li>+1 415 555 0142</li><li>hello@brightlane.co</li></ul></div>
    <div class="footer-col"><h5>NEWSLETTER</h5><p>Subscribe to our newsletter for fresh insights about our latest projects.</p><div class="newsletter">Email Address</div></div>
  </div>
  <div class="copyright">© 2024<b>Brightlane</b>All rights reserved</div>
</footer>

</body>
</html>
```